Aunt Ruwaida's Bakery

I am about to create a luxury boutique that specializes in cake baking and cupcake
and ready for parties and special events and order delivery
the logo has already made

Industry/Entity Type

Boutique

Contact Information for Business Card

Email:auntruwaidasbakery@mailvelo.com
Instagram: aunt_ruwaida_bakery
Twitter: xxxxxxx
WhatsApp: xxxxxxx

Requirements
Must have
• luxury design

```html
<!DOCTYPE html>
<html lang="en">
<head>
<meta charset="utf-8">
<title>Aunt Ruwaida's Bakery — Business Card</title>
<link rel="stylesheet" href="https://fonts.googleapis.com/css2?family=Nunito+Sans:wght@400;600&display=swap">
<style>
  :root {
    --backdrop: #e9e7e4;
    --card: #ffffff;
    --brand-grey: #7a7671;
    --brand-pink: #d993a3;
    --ink: #232323;
  }
  * { margin: 0; padding: 0; box-sizing: border-box; }
  html, body {
    width: 1200px;
    height: 800px;
    overflow: hidden;
    background: var(--backdrop);
    font-family: "Nunito Sans", Arial, sans-serif;
  }
  .canvas {
    width: 1200px;
    height: 800px;
    display: flex;
    align-items: center;
    justify-content: center;
  }
  .card {
    position: relative;
    width: 840px;
    height: 480px;
    background: var(--card);
    box-shadow: 0 2px 10px rgba(0,0,0,0.08);
  }
  .brand {
    position: absolute;
    left: 60px;
    top: 150px;
    width: 320px;
    display: flex;
    flex-direction: column;
    align-items: center;
    gap: 18px;
  }
  .brand-dot {
    width: 64px;
    height: 64px;
    border-radius: 50%;
    background: var(--brand-pink);
  }
  .brand-name {
    font-weight: 600;
    font-size: 30px;
    letter-spacing: 1px;
    color: var(--brand-grey);
    text-align: center;
    line-height: 1.2;
  }
  .divider-brace {
    position: absolute;
    left: 405px;
    top: 110px;
    width: 80px;
    height: 260px;
  }
  .contact-list {
    position: absolute;
    left: 515px;
    top: 190px;
    list-style: none;
    display: flex;
    flex-direction: column;
    gap: 8px;
  }
  .contact-item {
    display: flex;
    align-items: center;
    gap: 14px;
    font-size: 17px;
    color: var(--ink);
    line-height: 22px;
  }
  .contact-icon {
    width: 16px;
    height: 16px;
    flex: none;
  }
  .contact-icon.mark-circle {
    border-radius: 50%;
    background: var(--ink);
    width: 13px;
    height: 13px;
    margin: 0 1.5px;
  }
  .contact-icon.mark-square {
    border-radius: 3px;
    background: var(--ink);
    width: 13px;
    height: 13px;
    margin: 0 1.5px;
  }
</style>
</head>
<body>
<main class="canvas">
  <section class="card" aria-label="Aunt Ruwaida's Bakery business card">
    <div class="brand">
      <span class="brand-dot" aria-hidden="true"></span>
      <p class="brand-name">Aunt Ruwaida's Bakery</p>
    </div>

    <svg class="divider-brace" viewBox="0 0 80 260" aria-hidden="true">
      <path d="M70 4 C38 8 30 30 30 70 L30 104 C30 122 22 128 4 130 C22 132 30 138 30 156 L30 190 C30 230 38 252 70 256 L70 250 C48 244 44 228 44 190 L44 152 C44 138 36 132 24 130 C36 128 44 122 44 108 L44 70 C44 32 48 16 70 10 Z" fill="var(--brand-grey)"/>
    </svg>

    <ul class="contact-list">
      <li class="contact-item">
        <svg class="contact-icon" viewBox="0 0 16 16" aria-hidden="true">
          <rect x="1" y="3" width="14" height="10" fill="none" stroke="var(--ink)" stroke-width="1.6"/>
          <path d="M1.5 3.8 L8 9 L14.5 3.8" fill="none" stroke="var(--ink)" stroke-width="1.6"/>
        </svg>
        <span>auntruwaidasbakery@mailvelo.com</span>
      </li>
      <li class="contact-item">
        <span class="contact-icon mark-square" aria-hidden="true"></span>
        <span>aunt_ruwaida_bakery</span>
      </li>
      <li class="contact-item">
        <span class="contact-icon mark-circle" aria-hidden="true"></span>
        <span>xxxxxxxxxxxx</span>
      </li>
      <li class="contact-item">
        <span class="contact-icon mark-circle" aria-hidden="true"></span>
        <span>xxxxxxxxxxxx</span>
      </li>
    </ul>
  </section>
</main>
</body>
</html>
```